New Toothpaste brand needs a logo & packaging design

Our company is launching a new toothpaste and is looking for a logo and packaging design. The toothpaste brand is called Brivana. The packaging should have the same design quality as the major international brands, such as Lumora, Lumora Totalcare, Dentiva, Pexolo, Wind-rise, Marvest, etc. The dominant colors for our brand should be hues of blue, similar to other major brands. In addition, there should be a little bit of green to represent the "Fresh Mint Blast" flavor and the "Extracts of Aloe Vera" included in the ingredients.

There are typically 3 unique sides on a toothpaste box:

The face: Repeated on ~3 sides of the 4 faces of the box
The back: The 4th box face has the instructions for use, ingredients, company information, bar code/product info, and some branding elements.
The sides: Usually consisting of just the logo, flavor etc.

Please refer to existing brands such as Lumora, Lumora Total-care, and Dentiva for an example of typical box layout and elements.

Task Details:
Package Dimensions: 180 mm x 48 mm x 28 mm, 100 ml toothpaste tube
Brand Name: Brivana
Description: Fluoride Toothpaste
Flavor: Fresh Mint Blast
5 Actions: Protects against cavities and tartar, freshens breath, whitens teeth, and maintains healthy gums. These actions can also be made into a list like Lumora Total Care or Dentiva Max care. For instance, Strong Teeth, Fresh Breath, Whitening, Healthy Gums, Cavity and Tartar Protection.
Also contains whitening micro particles and extracts of aloe vera which may be highlighted on the package

Overall, the look should be high quality and with the same look and feel as the big brands mentioned previously. We do not have an existing logo for this brand. The face of the package is the most important element as it is often repeated on several sides and on the tube itself.

Please let me know if you have any questions.

I've attached some of our favorite big brand designs below. I would say the Lumora Total Care and Gleam vers

The logos I've seen so far for Brivana, have been a bit too bold. A little bold is okay, but just needs to be moderate. 

I would like the colors to be bright and appealing. I mentioned shades of blue being the major color, but green should also be highlighted as well, perhaps in a 80% blue to 20% green ratio. 

Target Market(s)

adult consumer of toothpaste, both female and male.

Industry/Entity Type

It Company

Requirements
Must have
• A logo with the brand name: Brivana
Description or sub text: Fluoride Toothpaste
Flavor: Fresh Mint Blast
A phrase or list describing the Toothpaste Actions: e.g., Protects against cavities and tartar, freshens breath, whitens teeth, and maintains healthy gums. Or as a list simialr to Lumora Total Care or Dentiva Max Care:
-Anti-cavity
-Anti-tartar
-Fresh breath
-Whitening
-Healthy Gums

Special ingredient of "whitening micro particles: and "extracts of aloe vera", which should also be highlighted.

The color should mostly be shades of blue, with only a little bit of green to accentuate the fresh mint blast flavor and aloe vera

Nice to have
• The design should really look good next to lumora total care, gleam pure, and dentiva max care. These are our favorite designs.
Should not have
• For aloe vera, there is no need to show the plant.

The Brivana logo shouldn't be too Bold. This should be appeal to all consumers, not just men.

```html
<!DOCTYPE html>
<html lang="en">
<head>
<meta charset="utf-8">
<title>Brivana Fluoride Toothpaste – Logo &amp; Pack Face</title>
<link rel="stylesheet" href="https://fonts.googleapis.com/css2?family=Fira+Sans:ital,wght@0,600;0,700;1,700&display=swap">
<style>
  :root {
    --navy: #2b3990;
    --deep-blue: #263c96;
    --bright-blue: #2a9fe0;
    --sky: #4fb8ec;
    --green: #5db53a;
    --lime: #8cc63f;
    --white: #ffffff;
    --page: #ffffff;
  }
  * { margin: 0; padding: 0; box-sizing: border-box; }
  html, body {
    width: 1200px;
    height: 1000px;
    overflow: hidden;
    background: var(--page);
    font-family: "Fira Sans", Arial, sans-serif;
  }
  .canvas {
    position: relative;
    width: 1200px;
    height: 1000px;
  }
  .brand-mark {
    position: absolute;
    left: 0;
    width: 1200px;
    top: 170px;
    text-align: center;
    font-size: 92px;
    font-weight: 700;
    line-height: 1;
    color: var(--navy);
    letter-spacing: -1px;
  }
  .pack-face {
    position: absolute;
    left: 180px;
    top: 423px;
    width: 700px;
    height: 187px;
    box-shadow: 0 3px 6px rgba(0,0,0,0.18);
    background: var(--white);
    overflow: hidden;
  }
  .pack-art {
    position: absolute;
    inset: 0;
  }
  .pack-name {
    position: absolute;
    left: 38px;
    top: 30px;
    font-size: 50px;
    font-weight: 700;
    line-height: 1;
    color: var(--navy);
    letter-spacing: -0.5px;
  }
  .pack-descriptor {
    position: absolute;
    left: 63px;
    top: 93px;
    font-size: 15px;
    font-weight: 600;
    color: var(--navy);
  }
  .ingredient-list {
    position: absolute;
    left: 64px;
    top: 140px;
    list-style: none;
    font-size: 12px;
    font-weight: 700;
    font-style: italic;
    line-height: 14px;
    color: var(--navy);
  }
  .ingredient-list li:last-child { padding-left: 16px; }
  .speed-line {
    position: absolute;
    height: 1px;
    background: var(--bright-blue);
  }
  .action-list {
    position: absolute;
    left: 562px;
    top: 23px;
    list-style: none;
    font-size: 13px;
    font-weight: 600;
    line-height: 16.5px;
    color: var(--white);
    letter-spacing: 0.3px;
  }
  .action-list li::before { content: "• "; }
  .flavour {
    position: absolute;
    left: 532px;
    top: 153px;
    font-size: 13px;
    font-weight: 700;
    font-style: italic;
    color: var(--white);
    letter-spacing: 0.3px;
  }
</style>
</head>
<body>
<main class="canvas">
  <h1 class="brand-mark">Brivana</h1>

  <section class="pack-face" aria-label="Brivana pack face">
    <svg class="pack-art" width="700" height="187" viewBox="0 0 700 187">
      <defs>
        <linearGradient id="panel-blue" x1="0" y1="0" x2="1" y2="0.3">
          <stop offset="0" stop-color="var(--bright-blue)"/>
          <stop offset="0.45" stop-color="#2f6ec1"/>
          <stop offset="1" stop-color="var(--deep-blue)"/>
        </linearGradient>
        <radialGradient id="sparkle-glow" cx="0.5" cy="0.5" r="0.5">
          <stop offset="0" stop-color="#ffffff" stop-opacity="0.28"/>
          <stop offset="1" stop-color="#ffffff" stop-opacity="0"/>
        </radialGradient>
        <linearGradient id="flavour-band" x1="0" y1="0" x2="1" y2="0">
          <stop offset="0" stop-color="var(--lime)"/>
          <stop offset="1" stop-color="var(--green)"/>
        </linearGradient>
      </defs>
      <polygon points="355,0 372,0 244,187 227,187" fill="var(--green)"/>
      <polygon points="372,0 700,0 700,187 244,187" fill="url(#panel-blue)"/>
      <polygon points="372,0 378,0 250,187 244,187" fill="var(--sky)"/>
      <ellipse role="img" aria-label="Sparkling starburst pattern" cx="440" cy="90" rx="170" ry="80" fill="url(#sparkle-glow)"/>
      <polygon points="530,152 700,152 700,173 516,173" fill="url(#flavour-band)"/>
    </svg>

    <div class="pack-name">Brivana</div>
    <div class="pack-descriptor">FLUORIDE TOOTHPASTE</div>

    <span class="speed-line" style="left:0;top:144px;width:60px"></span>
    <span class="speed-line" style="left:0;top:149px;width:60px"></span>
    <span class="speed-line" style="left:0;top:160px;width:76px"></span>
    <ul class="ingredient-list">
      <li>WHITENING MICRO PARTICLES</li>
      <li>EXTRACTS OF ALOE VERA</li>
    </ul>

    <ul class="action-list">
      <li>ANTI-CAVITY</li>
      <li>ANTI-TARTAR</li>
      <li>FRESH BREATH</li>
      <li>WHITENING</li>
      <li>HEALTHY GUMS</li>
    </ul>

    <div class="flavour">FRESH MINT BLAST</div>
  </section>
</main>
</body>
</html>
```